Business Card Re-Design...or logo does not look sharp

Hello

We are a start-up and just need someone to help us.

Our colors are: Delilah charm pink (yeah I know) and charcoal for the lettering.

I am attaching our logo which needs cleaning up.

We want the JUST the lady ironing on the table (pink) in front, and the background in charcoal. All the business info can be on the back.

Dims on card are 2 x 2''

Also, if you have better ideas....please let us know!

Thanks

Marcus

Business

Casa Brisa Dorada
4821 Pelham Ridge Dr Suite B2
El Paso TX 79958
915-555-0143

```html
<!DOCTYPE html>
<html lang="en">
<head>
<meta charset="utf-8">
<title>Casa Brisa Dorada — Business Card</title>
<link rel="stylesheet" href="https://fonts.googleapis.com/css2?family=Yellowtail&display=block">
<style>
  :root {
    --page: #ffffff;
    --charcoal: #232323;
    --pink: #e8368f;
    --script: "Yellowtail", "Brush Script MT", "Brush Script Std", "Segoe Script", cursive;
  }
  html, body {
    margin: 0;
    padding: 0;
    overflow: hidden;
  }
  body {
    width: 1200px;
    height: 1200px;
    background: var(--page);
    position: relative;
    font-family: var(--script);
  }
  .card {
    position: absolute;
    left: 263px;
    width: 678px;
    height: 397px;
    background: var(--charcoal);
  }
  .card--front { top: 54px; }
  .card--back  { top: 512px; }

  .card-art {
    position: absolute;
    inset: 0;
    width: 678px;
    height: 397px;
  }
  .card-art text {
    font-family: var(--script);
    fill: var(--pink);
    letter-spacing: 1px;
  }
  .front-name { font-size: 70px; }
  .front-emblem { fill: var(--pink); }

  .back-name { font-size: 60px; }
  .back-line { font-size: 46px; }
</style>
</head>
<body>
  <section class="card card--front">
    <svg class="card-art" viewBox="0 0 678 397" xmlns="http://www.w3.org/2000/svg">
      <defs>
        <path id="name-arc" d="M 42 178 Q 339 42 642 188" fill="none"/>
      </defs>
      <text class="front-name">
        <textPath href="#name-arc" startOffset="50%" text-anchor="middle">Casa Brisa Dorada</textPath>
      </text>
      <rect class="front-emblem" x="280" y="178" width="116" height="93"
            role="img" aria-label="Pink silhouette of a woman ironing at a table"/>
    </svg>
  </section>

  <section class="card card--back">
    <svg class="card-art" viewBox="0 0 678 397" xmlns="http://www.w3.org/2000/svg">
      <text class="back-name" x="339" y="112" text-anchor="middle">Casa Brisa Dorada</text>
      <text class="back-line" x="339" y="160" text-anchor="middle">4821 Pelham Ridge</text>
      <text class="back-line" x="339" y="208" text-anchor="middle">Dr Suite B2</text>
      <text class="back-line" x="339" y="256" text-anchor="middle">El Paso</text>
      <text class="back-line" x="339" y="302" text-anchor="middle">TX 79958 915-555-0143</text>
    </svg>
  </section>
</body>
</html>
```